****FLYER design - LAW FIRM ADVERTISEMENT****

We are a small law firm based in Los Angeles, CA. We need an flyer used for advertising that we will be passing out. We want the flyer to be about 4in x 6in.

We want the flyer to advertise the name of our firm: MARVELLO QUINTARD LLP (no period)
- We want our group photo to take up a good portion of the flyer (although it's okay if parts of the photo have wording over it.)

COLORS: Our firm colors are different shades of steal/metal grey with a bit of a bold orange accent. Any bold writing, like our slogan, names of practice areas,... should be in orange.

We envision a horizontal lay-out of the flyer, but are open to creative options laid out vertically!

Feel free to play with the fonts, the sizing, the color combinations,...

We want the flyer to advertise our two areas of practice: PERSONAL INJURY and EMPLOYMENT LAW. Please also place each photo icon of our areas of practice somewhere around the name (ambulance photo for personal injury; person behind computer desk for employment law). The icons can be relatively small.

Under Personal Injury, please write:
If you or a loved one are suffering from an injury or wrongful death caused by the careless or intentional acts of others, then you have the right to pursue compensation for your injury, out-of-pocket expenses, lost wages, emotional anguish, and more.

Under Employment Law, please write:
Our attorneys regularly represent clients in disputes involving sex, age and race discrimination, sexual harassment, retaliatory discharge, defamation, unlawful termination, breach of employment contracts, and more.

Somewhere on the flyer, please write our slogan IN ITALICS (and probably in orange):
- Your Voice. Our Fight. Your Win.

In somewhat bright and bold writing, please write "CONTACT US FOR A FREE CONSULTATION TODAY!" (maybe just after our slogan?)
- And under that phrase, write:
- 752 W. Folbrook Lane, Suite 400 Beverly Hills, CA 90210
phone: 310.555.8143
fax: 310.555.9261
email: info@mqmlegal.example
web: www.mqmlegal.example

If possible, and only if there's room without it looking too busy, somewhere in the upper left corner, place our "MQM" logo.
Updates

PLEASE NOTE THAT WE CHANGED OUR GROUP PHOTO TO A SLIGHTLY EDITED ONE.  PLEASE BE SURE TO USE THE NEW ONE!!!  (We deleted the old.)

Target Market(s)

employees, lower and mid-income individuals, minority communities. However, we still want the flyer to look sleek, modern, and professional.

Industry/Entity Type

Advertising

Requirements
Must have
• Firm Name,
Photo of Partners,
Names, photos, and small description of practice areas,
Firm slogan,
"Contact us for a free consultation today!",
Firm contact info.

And only if space and overall look permits, firm "MQM" logo.

We want an overall very sleek, modern feel to our flyer. While we do want to look professional, we wanted a more approachable feel than the typical, conservative law offices.
Nice to have
• Firm "MQM" logo

Horizontal lay out, though we're open to vertical options.

```html
<!DOCTYPE html>
<html lang="en">
<head>
<meta charset="utf-8">
<title>Marvello Quintard LLP — Flyer</title>
<link rel="stylesheet" href="https://fonts.googleapis.com/css2?family=Carlito:ital,wght@0,400;0,700;1,400;1,700&display=swap">
<style>
  :root {
    --steel: #5b6570;
    --orange: #e8602c;
    --white: #ffffff;
    --paper: #ffffff;
    --icon-bg: #2d3137;
  }
  * { margin: 0; padding: 0; box-sizing: border-box; }
  html, body { width: 933px; height: 1200px; overflow: hidden; background: var(--paper); }
  body { position: relative; font-family: "Carlito", "Calibri", sans-serif; color: var(--white); }

  .card { position: absolute; left: 65px; width: 801px; height: 532px; background: var(--steel); }
  .card-front { top: 54px; }
  .card-back { top: 618px; }

  /* front */
  .front-mark {
    position: absolute; left: 0; right: 0; top: 192px;
    text-align: center; font-weight: 400; font-size: 76px; letter-spacing: 12px; line-height: 1;
  }
  .front-name {
    position: absolute; left: 0; right: 0; top: 275px;
    text-align: center; font-weight: 700; font-size: 25px; line-height: 1;
  }
  .slogan { color: var(--orange); font-style: italic; font-weight: 700; }
  .front-slogan { position: absolute; left: 0; right: 0; top: 305px; text-align: center; font-size: 19px; line-height: 1; }

  /* back */
  .firm-name { position: absolute; left: 14px; top: 20px; font-size: 35px; font-weight: 700; line-height: 1; }
  .back-slogan { position: absolute; left: 53px; top: 60px; font-size: 19px; line-height: 1; }

  .practice { position: absolute; left: 17px; width: 400px; }
  .practice-injury { top: 96px; }
  .practice-employment { top: 322px; }
  .practice-head { display: flex; align-items: flex-end; gap: 12px; height: 38px; }
  .practice-icon { width: 31px; height: 31px; flex: none; }
  .practice-title { color: var(--orange); font-size: 30px; font-weight: 700; line-height: 1; }
  .practice-text { font-size: 19.5px; line-height: 26.5px; margin-top: 4px; width: 392px; }

  .team-photo {
    position: absolute; left: 430px; top: 0; width: 371px; height: 281px;
    background: linear-gradient(100deg, #c9b59a 0%, #8a6f52 25%, #2b2b30 45%, #efe9e3 62%, #3a2a22 75%, #b89d7c 100%);
  }

  .contact { position: absolute; left: 430px; top: 281px; width: 371px; text-align: center; }
  .contact-cta { color: var(--orange); font-weight: 700; font-size: 23px; line-height: 30px; margin-top: 9px; }
  .contact-details { font-weight: 700; font-size: 17.5px; line-height: 24.5px; margin-top: 8px; }

  .corner-mark { position: absolute; right: 18px; bottom: 26px; font-size: 13px; font-weight: 400; letter-spacing: 1px; }
</style>
</head>
<body>
  <section class="card card-front">
    <div class="front-mark">MQM</div>
    <div class="front-name">MARVELLO QUINTARD LLP</div>
    <div class="front-slogan slogan">Your Voice. Our Fight. Your Win.</div>
  </section>

  <section class="card card-back">
    <h1 class="firm-name">MARVELLO QUINTARD LLP</h1>
    <p class="back-slogan slogan">Your Voice. Our Fight. Your Win.</p>

    <div class="practice practice-injury">
      <div class="practice-head">
        <svg class="practice-icon" viewBox="0 0 21 21" aria-hidden="true">
          <rect width="21" height="21" fill="#2d3137"/>
          <rect x="3" y="7" width="11" height="7" fill="#fff"/>
          <path d="M14 9h3l2 3v2h-5z" fill="#fff"/>
          <circle cx="6" cy="15" r="1.6" fill="#fff"/><circle cx="16" cy="15" r="1.6" fill="#fff"/>
          <path d="M8 9h1v1.2h1.2v1H9v1.2H8v-1.2H6.8v-1H8z" fill="#2d3137"/>
        </svg>
        <h2 class="practice-title">Personal Injury</h2>
      </div>
      <p class="practice-text">If you or a loved one are suffering from an injury or wrongful death caused by the careless or intentional acts of others, then you have the right to pursue compensation for your injury, out-of-pocket expenses, lost wages, emotional anguish, and more.</p>
    </div>

    <div class="practice practice-employment">
      <div class="practice-head">
        <svg class="practice-icon" viewBox="0 0 21 21" aria-hidden="true">
          <rect width="21" height="21" fill="#2d3137"/>
          <circle cx="6" cy="6" r="2" fill="#fff"/>
          <rect x="4.5" y="8.5" width="3" height="6" fill="#fff"/>
          <rect x="9" y="7" width="7" height="5" fill="#fff"/>
          <rect x="3" y="14" width="15" height="1.5" fill="#fff"/>
          <rect x="4" y="15.5" width="1.3" height="3" fill="#fff"/><rect x="15.7" y="15.5" width="1.3" height="3" fill="#fff"/>
        </svg>
        <h2 class="practice-title">Employment Law</h2>
      </div>
      <p class="practice-text">Our attorneys regularly represent clients in disputes involving sex, age and race discrimination, sexual harassment, retaliatory discharge, defamation, unlawful termination, breach of employment contracts, and more.</p>
    </div>

    <div class="team-photo" role="img" aria-label="Group photo of the firm's three partners standing in an office lobby"></div>

    <div class="contact">
      <p class="contact-cta">"CONTACT US FOR A FREE<br>CONSULTATION TODAY!"</p>
      <p class="contact-details">
        752 W. Folbrook Lane,<br>
        Suite 400 Beverly Hills, CA 90210<br>
        phone: 310.555.8143<br>
        fax: 310.555.9261<br>
        email: info@mqmlegal.example<br>
        web: www.mqmlegal.example
      </p>
    </div>

    <div class="corner-mark">MQM</div>
  </section>
</body>
</html>
```